UI design for Fast Food Restaurant Self-Order App

Background:
App purpose: for fast food restaurant customers to self order food/drink by choosing item image, and make payment by tapping the credit card on the card terminal.
Reference: https://www.brivolkiosks.example/product-overview/self-order-kiosks/
Attachment:
Wireframes. (wire frames provide general idea and the information to display, they are not a strict guideline for layout design.)
Tarrowby's Self ordering app.
Intro:
We have built a (for restaurant and cafe) Self Ordering and Payment app, similar to Tarrowby's self ordering software in most of their new restaurants. Our app will be placed in a Quorvane Deskline 10 OS touch screen Kiosk(screen size 4:3 or Portrait 16:9) within the restaurant/cafe premise.
Pages to be designed:
Page 1. Food Browsing Page. displays all food images(to be provided by cafes) by categories, and displays the Cart. This page will lead to Page 2 or Page 3.
'Cart' section should include:
'cart items/selected items', its quantity and price. like Tarrowbys' app.
When click on a Cart Item, we need to allow to change quantity or 'change Choice'. The UI handling these change requests with ease will be one deciding factor for us to choose your design.
Fact: up to 10 food categories, and 10 - 25 food items under each categories.
When click on one item image, it goes to Page 2.
Page 2. Item Detail/Description Page. Shows description of the food, and its available Choice(other food items or Special Request, up to 12) will also be displayed. 'Add item to cart' action(Button Name: ADD) will happen here and go back to Browsing Page 1.
e.g. Item 'Fried Rice' Page. the Choice could be 'Add Egg', 'Add Meat', 'No Chilli' etc.
Page 3. Order Review Page. No edit features allowed on this page, only two buttons: 'No' to go back to Browsing Page, or 'Yes' to proceed to Payment Page 4. Check Tarrowby's screen.
Page 4. Payment Page - Prompt user to Insert or Tap credit card on the credit card terminal. (Exact wording: PLEASE FOLLOW INSTRUCTIONS DISPLAYED ON CREDIT CARD TERMINAL BELOW)
Page 5. Payment status. Successful / Failed.
Our considerations to pick the winner:
1. In terms of design for this task, we look out for page layout, effects, fonts, button style and overall colour scheme. the design should present itself in a clean and modern look, with minimum clicking or scrolling. The app aims to help customers choose and pay for their items quickly.
2.we need to handle both 4:3(as shown in wire frames) and 16:9 screens(like Tarrowby's). there will be a lot more vertical space to utilise when it is in 16:9, resulting less scrolling than 4:3. tell us what you think.
All questions are welcome.
Winner has opportunity to work on a few more app UI. Cheers!
Industry/Entity Type
Fast Food Restaurant
Requirements
Must have
- Button colour differentiation - helps people know what to click next.
- best use of screen space. minimum click and scrolls.
Nice to have
- any personal touch.
Should not have
- unrelated design pattern, e.g. a cute animal or flower pattern in the layout.

```html
<!DOCTYPE html>
<html lang="en">
<head>
<meta charset="utf-8">
<title>Pellamy Self-Order Kiosk – UI Screens</title>
<link rel="stylesheet" href="https://fonts.googleapis.com/css2?family=Raleway:wght@300;400;500;600;700;800&display=swap">
<style>
  :root{
    --stage:#6e665c;
    --panel:#ffffff;
    --panel-soft:#f4f4f4;
    --ink:#111111;
    --muted:#9a9a9a;
    --faint:#c4c4c4;
    --rule:#1a1a1a;
    --cart:#efefef;
    --blue:#1bb0e0;
    --green:#1dbf9a;
    --grey-btn:#e3e3e3;
    --grey-btn-text:#9d9d9d;
    --alert:#e4205b;
  }
  *{box-sizing:border-box;margin:0;padding:0}
  html,body{width:1053px;height:1200px;overflow:hidden;background:var(--stage)}
  body{position:relative;font-family:"Raleway",Arial,sans-serif;color:var(--ink)}
  .screen{position:absolute;width:488px;height:366px;background:var(--panel);overflow:hidden}
  .screen.soft{background:var(--panel-soft)}
  .abs{position:absolute}

  /* brand */
  .brand-disc{position:absolute;left:6px;top:8px;width:56px;height:56px;border-radius:50%;background:#fff;box-shadow:0 0 0 1px #ececec;display:flex;align-items:center;justify-content:center;font-weight:800;font-size:9px;letter-spacing:.5px}
  .brand-tab{position:absolute;left:217px;top:0;width:56px;height:64px;background:#fff;clip-path:polygon(0 0,100% 0,100% 100%,50% 88%,0 100%);display:flex;align-items:center;justify-content:center;font-weight:800;font-size:9px;letter-spacing:.5px}

  /* side navigation */
  .nav{position:absolute;left:0;top:70px;width:62px}
  .nav .head{font-size:9px;font-weight:400;text-align:right;border-bottom:1.5px solid var(--rule);padding-bottom:1px}
  .nav .item{font-size:5.5px;text-align:right;height:23.5px;padding-top:12px;border-bottom:1px solid #555;font-weight:500}
  .nav .item.on{font-weight:800}
  .nav.dim .head,.nav.dim .item{color:var(--faint);border-color:#d8d8d8}

  /* menu grid */
  .grid-title{position:absolute;left:166px;top:14px;font-size:12px;font-weight:400}
  .grid-title small{font-size:6px;font-weight:600}
  .tile{position:absolute;width:90px}
  .tile .photo{height:66px}
  .tile .name{font-size:6.5px;font-weight:700;text-align:center;margin-top:5px;line-height:1.15}
  .price{color:var(--muted);font-weight:400;font-size:5px}
  .tone-a{background:linear-gradient(135deg,#c57a3c,#4f5a2a)}
  .tone-b{background:linear-gradient(135deg,#2b2b2b,#d77d2a)}
  .tone-c{background:linear-gradient(135deg,#e8dcc4,#e7b53a)}
  .tone-d{background:linear-gradient(135deg,#6a4a2a,#e0b64a)}
  .tone-e{background:linear-gradient(135deg,#3a3a3a,#e07a55)}
  .tone-f{background:linear-gradient(135deg,#d2a45a,#b84a2e)}
  .tone-g{background:linear-gradient(135deg,#3a2418,#6b7a4a)}
  .tone-h{background:linear-gradient(135deg,#d9b26a,#8a5a2e)}
  .tone-i{background:linear-gradient(135deg,#dfe6e2,#7ea24c)}
  .tone-j{background:linear-gradient(135deg,#3e5a2a,#e07a3c)}
  .tone-k{background:linear-gradient(135deg,#b8c66a,#6a4a3a)}
  .tone-l{background:linear-gradient(135deg,#d8c79a,#f1c232)}

  /* cart */
  .cart{position:absolute;left:372px;top:0;width:116px;height:196px;background:var(--cart);clip-path:polygon(0 0,100% 0,100% 100%,50% 172px,0 100%)}
  .cart h3{font-size:8px;font-weight:800;text-align:center;margin-top:14px;padding-bottom:3px;border-bottom:2px solid var(--rule);margin-left:5px;margin-right:5px}
  .cart-line{position:absolute;left:5px;width:106px;font-size:5.5px;font-weight:700}
  .cart-line .x{display:inline-block;width:6px;height:6px;border:1px solid var(--alert);border-radius:50%;vertical-align:middle;margin-right:3px}
  .cart-line .qty{position:absolute;left:66px;top:-1px;background:#fff;padding:1px 3px}
  .cart-line .amt{position:absolute;right:0;top:0;color:var(--muted);font-weight:400}
  .cart-sub{position:absolute;left:17px;font-size:5px;line-height:8px}
  .cart-sub .link{color:var(--blue);font-size:4.5px}
  .btn{position:absolute;border-radius:13px;display:flex;align-items:center;justify-content:center;font-weight:800;color:#fff;font-size:8.5px}
  .btn.grey{background:var(--grey-btn);color:var(--grey-btn-text)}
  .btn.blue{background:var(--blue)}
  .btn.green{background:var(--green)}

  /* item detail */
  .opt{position:absolute;width:60px}
  .opt .photo{height:44px;position:relative}
  .opt .photo.sel{outline:1.5px solid var(--blue)}
  .opt .photo.sel::after{content:"";position:absolute;right:1px;bottom:1px;width:8px;height:8px;background:var(--blue)}
  .opt .name{font-size:5.5px;font-weight:600;text-align:center;margin-top:2px;line-height:1.2}

  /* review */
  .dbl{position:absolute;left:77px;width:334px;height:4px;border-top:2px solid var(--rule);border-bottom:1px solid var(--rule)}
  .row{position:absolute;left:77px;width:334px;height:26px}
  .row .thumb{position:absolute;left:0;top:0;width:35px;height:26px}
  .row .nm{position:absolute;left:39px;top:2px;font-size:8.5px;font-weight:700}
  .row .opts{position:absolute;left:48px;top:16px;font-size:5.5px}
  .row .q{position:absolute;left:276px;top:3px;font-size:7.5px;font-weight:600}
  .row .p{position:absolute;right:0;top:2px;font-size:8.5px;font-weight:700}

  .status-title{position:absolute;left:0;width:488px;text-align:center;font-size:26px;font-weight:300;letter-spacing:.5px}
  .status-sub{position:absolute;left:0;width:488px;text-align:center;font-size:12px;font-weight:400}
</style>
</head>
<body>

<!-- Browsing -->
<section class="screen" style="left:26px;top:26px">
  <div class="brand-disc">PELLAMY</div>
  <nav class="nav">
    <div class="head">MENU</div>
    <div class="item">CHRISTMAS</div>
    <div class="item">MINI CAKES</div>
    <div class="item">WHOLE CAKES</div>
    <div class="item on">MAIN</div>
    <div class="item">ADD-ONS</div>
  </nav>
  <div class="grid-title">MAINS <small>(15)</small></div>
  <svg class="abs" style="left:330px;top:18px" width="28" height="8" viewBox="0 0 28 8" fill="none" stroke="#111" stroke-width="1"><path d="M1 2l5 5 5-5M17 7l5-5 5 5"/></svg>

  <div class="tile" style="left:77px;top:38px"><div class="photo tone-a" role="img" aria-label="Big breakfast plate photo"></div><div class="name">Triple B <span class="price">/ $20.00</span></div></div>
  <div class="tile" style="left:172px;top:38px"><div class="photo tone-b" role="img" aria-label="Steak skewer photo"></div><div class="name">Steak Are High <span class="price">/ $20.00</span></div></div>
  <div class="tile" style="left:267px;top:38px"><div class="photo tone-c" role="img" aria-label="Eggs benedict photo"></div><div class="name">Eggs Benedict <span class="price">/ $16.00</span></div></div>

  <div class="tile" style="left:77px;top:130px"><div class="photo tone-d" role="img" aria-label="Pulled pork eggs benedict photo"></div><div class="name">Pulled Pork Eggs Benedict<br><span class="price">/ $19.00</span></div></div>
  <div class="tile" style="left:172px;top:130px"><div class="photo tone-e" role="img" aria-label="Smoked salmon croissant photo"></div><div class="name">Smoked Salmon Croissant<br><span class="price">/ $17.00</span></div></div>
  <div class="tile" style="left:267px;top:130px"><div class="photo tone-f" role="img" aria-label="Fish and chips photo"></div><div class="name">Fisherman's Dory with<br>Fires <span class="price">/ $18.00</span></div></div>

  <div class="tile" style="left:77px;top:230px"><div class="photo tone-g" role="img" aria-label="Pan seared salmon photo"></div><div class="name">Pan Seared Norwegian<br>Salmon <span class="price">/ $19.00</span></div></div>
  <div class="tile" style="left:172px;top:230px"><div class="photo tone-h" role="img" aria-label="Prawn pasta photo"></div><div class="name">Prawn Aglio Olio <span class="price">/ $18.00</span></div></div>
  <div class="tile" style="left:267px;top:230px"><div class="photo tone-i" role="img" aria-label="Guacamole breakfast photo"></div><div class="name">Guacamole Breakfast<br><span class="price">/ $16.00</span></div></div>

  <div class="tile" style="left:77px;top:329px"><div class="photo tone-j" role="img" aria-label="Salad dish photo"></div></div>
  <div class="tile" style="left:172px;top:329px"><div class="photo tone-k" role="img" aria-label="Roast chicken dish photo"></div></div>
  <div class="tile" style="left:267px;top:329px"><div class="photo tone-l" role="img" aria-label="Egg dish photo"></div></div>

  <aside class="cart">
    <h3>MY ORDER</h3>
    <div class="cart-line" style="top:40px"><span class="x"></span>Triple B<span class="qty">x 1</span><span class="amt">$20.50</span></div>
    <div class="cart-sub" style="top:49px">Poached Egg<br>Ragout Mushroom<br>Brioche<br><span class="link">CHANGE OPTIONS &gt;</span></div>
    <div class="abs" style="left:14px;top:50px;width:1px;height:28px;background:#ccc"></div>
    <div class="cart-line" style="top:96px"><span class="x"></span>Steak Are High<span class="qty">x 1</span><span class="amt">$20.00</span></div>
    <div class="abs" style="left:5px;top:112px;width:106px;height:3px;border-top:1.5px solid var(--rule);border-bottom:1px solid var(--rule)"></div>
    <div class="abs" style="right:5px;top:120px;font-size:5.5px;font-weight:600">TOTAL: <b style="font-size:9px;font-weight:800">$40.50</b></div>
    <div class="btn grey" style="left:5px;top:138px;width:52px;height:20px;font-size:6.5px">CANCEL</div>
    <div class="btn green" style="left:59px;top:138px;width:52px;height:20px;font-size:6.5px">DONE</div>
  </aside>
</section>

<!-- Item detail -->
<section class="screen" style="left:539px;top:26px">
  <div class="brand-disc">PELLAMY</div>
  <nav class="nav dim">
    <div class="head">MENU</div>
    <div class="item">CHRISTMAS</div>
    <div class="item">MINI CAKES</div>
    <div class="item">WHOLE CAKES</div>
    <div class="item">MAIN</div>
    <div class="item">ADD-ONS</div>
  </nav>
  <div class="abs tone-a" style="left:78px;top:30px;width:137px;height:104px" role="img" aria-label="Big breakfast plate photo"></div>
  <div class="abs" style="left:222px;top:47px;font-size:12px;font-weight:800">Triple B <span style="font-size:6px;font-weight:600">/ $20.00</span></div>
  <p class="abs" style="left:222px;top:67px;width:262px;font-size:9.6px;line-height:12.8px;font-weight:400">Pellamy's Big Breakfast. Freshly baked buttery croissant served with scrambled eggs, assorted sausages, honey-glazed bacon, sauteed mushroom &amp; fresh greens.</p>
  <div class="abs" style="left:91px;top:148px;font-size:8.5px">OPTIONS <span style="font-size:5.5px;font-weight:600">(12)</span></div>
  <div class="abs" style="left:85px;top:146px;width:1px;height:152px;background:#ddd"></div>

  <div class="opt" style="left:91px;top:164px"><div class="photo sel tone-d" role="img" aria-label="Brioche photo"></div><div class="name">Brioche <span class="price">/ $0.50</span></div></div>
  <div class="opt" style="left:155px;top:164px"><div class="photo tone-h" role="img" aria-label="Sourdough slice photo"></div><div class="name">Sourdough Slice<br><span class="price">/ $0.50</span></div></div>
  <div class="opt" style="left:219px;top:164px"><div class="photo sel tone-l" role="img" aria-label="Poached egg photo"></div><div class="name">Poached Egg</div></div>
  <div class="opt" style="left:283px;top:164px"><div class="photo tone-c" role="img" aria-label="Sunny side up egg photo"></div><div class="name">Sunny Side Up</div></div>
  <div class="opt" style="left:347px;top:164px"><div class="photo tone-j" role="img" aria-label="Chicken cheese sausage photo"></div><div class="name">2 Chicken Cheese Sausage <span class="price">/ $1.00</span></div></div>
  <div class="opt" style="left:411px;top:164px"><div class="photo tone-f" role="img" aria-label="Pork garlic sausage photo"></div><div class="name">2 Pork French Garlic Sausage</div></div>

  <div class="opt" style="left:91px;top:232px"><div class="photo sel tone-g" role="img" aria-label="Ragout mushroom photo"></div><div class="name">Ragout Mushroom</div></div>
  <div class="opt" style="left:155px;top:232px"><div class="photo tone-e" role="img" aria-label="Smoked salmon photo"></div><div class="name">+ Smoked Salmon<br><span class="price">/ $5.00</span></div></div>
  <div class="opt" style="left:219px;top:232px"><div class="photo tone-k" role="img" aria-label="Honey baked ham photo"></div><div class="name">+ Honey Baked Ham <span class="price">/ $4.00</span></div></div>
  <div class="opt" style="left:283px;top:232px"><div class="photo tone-h" role="img" aria-label="Hashbrowns photo"></div><div class="name">+ Triangular Hashbrowns <span class="price">/ $3.50</span></div></div>
  <div class="opt" style="left:347px;top:232px"><div class="photo" style="background:linear-gradient(135deg,#e6e6e6,#f7d7e0)" role="img" aria-label="Mini cake photo"></div><div class="name">+ Mini Unicorn Cake<br><span class="price">/ $9.00</span></div></div>
  <div class="opt" style="left:411px;top:232px"><div class="photo" style="background:linear-gradient(135deg,#dfe3ea,#3d5aa8)" role="img" aria-label="Blue glazed cake photo"></div><div class="name">+ Moon Drop <span class="price">/ $8.50</span></div></div>

  <div class="btn grey" style="left:144px;top:324px;width:127px;height:25px">GO BACK</div>
  <div class="btn blue" style="left:278px;top:324px;width:128px;height:25px">ADD TO LIST</div>
</section>

<!-- Order review -->
<section class="screen soft" style="left:26px;top:417px">
  <div class="brand-tab">PELLAMY</div>
  <h2 class="abs" style="left:0;width:488px;text-align:center;top:77px;font-size:12.5px;font-weight:800">ORDER REVIEW</h2>
  <div class="dbl" style="top:94px"></div>
  <div class="row" style="top:109px"><div class="thumb tone-a" role="img" aria-label="Big breakfast thumbnail"></div><div class="nm">Triple B</div><div class="opts">Brioche / Poached Egg / Ragout Mushroom</div><div class="q">x 1</div><div class="p">$20.50</div></div>
  <div class="row" style="top:145px"><div class="thumb tone-b" role="img" aria-label="Steak skewer thumbnail"></div><div class="nm">Steak Are High</div><div class="q">x 1</div><div class="p">$20.00</div></div>
  <div class="row" style="top:176px"><div class="thumb" style="background:linear-gradient(135deg,#f1c070,#e08a2a)" role="img" aria-label="Truffle fries thumbnail"></div><div class="nm">Truffle Fries</div><div class="q">x 2</div><div class="p">$22.00</div></div>
  <div class="row" style="top:207px"><div class="thumb" style="background:linear-gradient(135deg,#e6e6e6,#f7d7e0)" role="img" aria-label="Mini cake thumbnail"></div><div class="nm">Mini Unicorn Cake</div><div class="q">x 2</div><div class="p">$18.00</div></div>
  <div class="row" style="top:238px"><div class="thumb" style="background:linear-gradient(135deg,#dfe3ea,#3d5aa8)" role="img" aria-label="Blue glazed cake thumbnail"></div><div class="nm">Moon Drop</div><div class="q">x 1</div><div class="p">$8.50</div></div>
  <div class="dbl" style="top:267px"></div>
  <div class="abs" style="right:77px;top:277px;font-size:7.5px;font-weight:600">TOTAL: <b style="font-size:12.5px;font-weight:800">$89.00</b></div>
  <div class="btn grey" style="left:114px;top:312px;width:128px;height:25px">GO BACK</div>
  <div class="btn green" style="left:247px;top:312px;width:128px;height:25px">READY TO PAY</div>
</section>

<!-- Payment -->
<section class="screen soft" style="left:539px;top:417px">
  <div class="brand-tab">PELLAMY</div>
  <div class="dbl" style="top:95px"></div>
  <svg class="abs" style="left:166px;top:121px" width="166" height="106" viewBox="0 0 166 106" fill="none" stroke="#111" stroke-width="3.5" role="img" aria-label="Secure card payment icon">
    <rect x="2" y="2" width="150" height="100" rx="6"/>
    <rect x="94" y="14" width="44" height="28"/>
    <rect x="18" y="68" width="26" height="12"/>
    <rect x="48" y="68" width="26" height="12"/>
    <path d="M78 68h28v12H78z"/>
    <path d="M134 64l20 7v14c0 10-8 16-20 20-12-4-20-10-20-20V71z" fill="#f4f4f4"/>
    <rect x="127" y="80" width="14" height="10" fill="#111" stroke="none"/>
    <path d="M129 80v-4a5 5 0 0 1 10 0v4" stroke-width="2.2"/>
  </svg>
  <p class="abs" style="left:0;width:488px;text-align:center;top:240px;font-size:12.2px;font-weight:800;line-height:14.5px">PLEASE FOLLOW INSTRUCTIONS DISPLAYED<br>ON CREDIT CARD TERMINAL BELOW</p>
  <div class="dbl" style="top:288px"></div>
</section>

<!-- Success -->
<section class="screen soft" style="left:26px;top:808px">
  <div class="brand-tab">PELLAMY</div>
  <svg class="abs" style="left:204px;top:116px" width="100" height="84" viewBox="0 0 100 84" fill="none" stroke="var(--green)" stroke-width="3.5">
    <path d="M85 30A38 38 0 1 1 70 15"/>
    <path d="M18 40l22 20 54-40"/>
  </svg>
  <div class="status-title" style="top:206px">SUCCESS!</div>
  <div class="status-sub" style="top:233px">Your order will be ready very soon.</div>
</section>

<!-- Error -->
<section class="screen soft" style="left:539px;top:808px">
  <div class="brand-tab">PELLAMY</div>
  <svg class="abs" style="left:198px;top:118px" width="94" height="78" viewBox="0 0 94 78" fill="none" stroke="var(--alert)" stroke-width="2.5">
    <path d="M47 3L91 75H3z"/>
    <path d="M47 28v24" stroke-width="4"/>
    <circle cx="47" cy="60" r="2.2" fill="var(--alert)" stroke="none"/>
  </svg>
  <div class="status-title" style="top:206px">ERROR</div>
  <div class="status-sub" style="top:233px">Please contact staff for assistance.</div>
</section>

</body>
</html>
```